Biotech company needs graphics to describe company culture

We would like to have help in describing our company culture in a graphic way.Our "local culture" focus areas (Proud & Accountable, Challenge & Collaborate) builds on the Halvern Quist corporate values which is Integrity, Intensity, Innovation and Involvement. Our "local norms" is describing behaviours which we want to see more of, and that will ensure that we get better at our culture focus. We would like this to be expressed in a graphic way, getting an image we can use for multiple purposes in a format that fits into PowerPoint slides, can be printed on mousepads etc. We want one Norwegian and one English version. Attached is an example of the desired content in both languages.

Target Market(s)

Employees

Industry/Entity Type

Biotechnology

Font styles to use
Serif

Colors

Designer to choose colors to be used in the design.

Requirements
Nice to have
• Want the employees to intuitive understand the connection from values to cultural focus to norms. The norms are the most important to highlight to our employees. They should understand that if they do more of the desired behaviours (norms), then they will have act according to our culture focus and our values.

```html
<!DOCTYPE html>
<html lang="en">
<head>
<meta charset="utf-8">
<title>Our Culture</title>
<link rel="stylesheet" href="https://fonts.googleapis.com/css2?family=Oswald:wght@500;600&family=Montserrat:wght@700;800&display=swap">
<style>
  :root {
    --stage: #6f7072;
    --paper: #ffffff;
    --footer-band: #e4e5e7;
    --red: #ef3e33;
    --navy: #2e3484;
    --charcoal: #333333;
    --ink: #111111;
    --norm-card: #e6e7e9;
    --connector: #e3e3e3;
    --accent-blue: #1f6fb8;
    --text-dark: #2a2d3a;
  }
  html, body { margin: 0; padding: 0; width: 1200px; height: 953px; overflow: hidden; background: var(--stage); }
  .culture-board { display: block; width: 1200px; height: 953px; }
  .display { font-family: "Oswald", "Arial Narrow", sans-serif; font-weight: 600; }
  .label { font-family: "Montserrat", Arial, sans-serif; font-weight: 800; }
  .norm-text { font-family: "Montserrat", Arial, sans-serif; font-weight: 800; font-size: 13.6px; fill: var(--text-dark); }
  .hl-blue { fill: var(--accent-blue); }
  .hl-red { fill: var(--red); }
  .hl-navy { fill: var(--navy); }
</style>
</head>
<body>
<svg class="culture-board" viewBox="0 0 1273 1011" xmlns="http://www.w3.org/2000/svg" aria-labelledby="board-title">
  <title id="board-title">Our Culture: values, culture focus and norms</title>

  <!-- slide -->
  <rect x="137" y="153" width="1000" height="707" fill="var(--paper)"/>
  <rect x="137" y="820" width="1000" height="40" fill="var(--footer-band)"/>
  <path d="M499 153 H777 V167 Q777 181 763 181 H513 Q499 181 499 167 Z" fill="var(--red)"/>

  <text class="display" x="505" y="255" font-size="68" fill="var(--ink)" textLength="267" lengthAdjust="spacingAndGlyphs">OUR&#160; CULTURE</text>

  <!-- column headers -->
  <g class="column-headers">
    <polygon points="137,275 457,275 465,304 457,333 137,333" fill="var(--red)"/>
    <polygon points="461,275 804,275 812,304 804,333 461,333 469,304" fill="var(--navy)"/>
    <polygon points="808,275 1137,275 1137,333 808,333 816,304" fill="var(--charcoal)"/>
    <g class="display" font-size="31" font-weight="500" fill="#fff">
      <text x="263" y="315" textLength="117" lengthAdjust="spacingAndGlyphs">OUR VALUES</text>
      <text x="542" y="315" textLength="195" lengthAdjust="spacingAndGlyphs">OUR CULTURE FOCUS</text>
      <text x="907" y="315" textLength="114" lengthAdjust="spacingAndGlyphs">OUR NORMS</text>
    </g>
  </g>

  <!-- connectors -->
  <g class="connectors" fill="none" stroke="var(--connector)" stroke-width="4">
    <path d="M407 470 H441 M407 543 H441 M407 614 H441 M407 682 H441 M441 470 V682 M441 585 H502"/>
    <path d="M526 470 H502 V685 H526 M502 540 H526 M502 609 H526"/>
    <path d="M707 470 H738 V685 H707 M707 540 H738 M707 609 H738 M738 584 H778"/>
    <path d="M834 423 H778 V743 H834 M778 583 H830"/>
  </g>
  <circle cx="474" cy="585" r="9" fill="var(--red)"/>
  <circle cx="778" cy="583" r="9" fill="var(--red)"/>

  <!-- values -->
  <g class="values">
    <g fill="var(--red)">
      <path d="M250 446 H407 V495 H250 A24.5 24.5 0 0 1 250 446 Z"/>
      <path d="M250 518 H407 V567 H250 A24.5 24.5 0 0 1 250 518 Z"/>
      <path d="M250 590 H407 V639 H250 A24.5 24.5 0 0 1 250 590 Z"/>
      <path d="M250 658 H407 V707 H250 A24.5 24.5 0 0 1 250 658 Z"/>
    </g>
    <g class="label" font-size="18" fill="#fff" text-anchor="middle">
      <text x="318" y="475">INTEGRITY</text>
      <text x="323" y="550">INTENSITY</text>
      <text x="319" y="622">INNOVATION</text>
      <text x="320" y="691">INVOLVEMENT</text>
    </g>
  </g>

  <!-- culture focus -->
  <g class="focus">
    <g fill="var(--navy)">
      <path d="M550 446 H707 V495 H550 A24.5 24.5 0 0 1 550 446 Z"/>
      <path d="M550 516 H707 V565 H550 A24.5 24.5 0 0 1 550 516 Z"/>
      <path d="M550 585 H707 V634 H550 A24.5 24.5 0 0 1 550 585 Z"/>
      <path d="M550 658 H707 V707 H550 A24.5 24.5 0 0 1 550 658 Z"/>
    </g>
    <g class="label" font-size="14.5" font-weight="700" fill="#fff" text-anchor="middle">
      <text x="615" y="477">PROUD</text>
      <text x="621" y="545">ACCOUNTABLE</text>
      <text x="618" y="614">CHALLENGE</text>
      <text x="616" y="688">COLLABORATE</text>
    </g>
  </g>

  <!-- norms -->
  <g class="norms">
    <rect x="834" y="368" width="218" height="113" rx="14" fill="var(--norm-card)"/>
    <path d="M1012 364 H1038 Q1052 364 1052 378 V471 Q1052 485 1038 485 H1018 C998 450 996 400 1012 364 Z" fill="var(--charcoal)"/>
    <text class="display" x="1015" y="442" font-size="42" font-weight="500" fill="#fff" textLength="27" lengthAdjust="spacingAndGlyphs">01</text>
    <text class="norm-text">
      <tspan x="849" y="395">I TAKE OWNERSHIP,</tspan>
      <tspan x="849" y="412">AM <tspan class="hl-blue">SOLUTION</tspan></tspan>
      <tspan x="849" y="429"><tspan class="hl-blue">ORIENTED</tspan> AND</tspan>
      <tspan x="849" y="445">ENSURES</tspan>
      <tspan x="849" y="462">IMPLEMENTATION</tspan>
    </text>

    <rect x="830" y="527" width="222" height="113" rx="14" fill="var(--norm-card)"/>
    <path d="M1012 525 H1038 Q1052 525 1052 539 V632 Q1052 646 1038 646 H1018 C998 611 996 561 1012 525 Z" fill="var(--red)"/>
    <text class="display" x="1012" y="602" font-size="42" font-weight="500" fill="#fff" textLength="30" lengthAdjust="spacingAndGlyphs">02</text>
    <text class="norm-text">
      <tspan x="849" y="575">I GIVE AND SEEK</tspan>
      <tspan x="849" y="591" class="hl-red">CONSTRUCTIVE</tspan>
      <tspan x="849" y="608" class="hl-red">FEEDBACK</tspan>
    </text>

    <rect x="832" y="687" width="220" height="113" rx="14" fill="var(--norm-card)"/>
    <path d="M1012 683 H1038 Q1052 683 1052 697 V790 Q1052 804 1038 804 H1018 C998 769 996 719 1012 683 Z" fill="var(--navy)"/>
    <text class="display" x="1013" y="762" font-size="42" font-weight="500" fill="#fff" textLength="30" lengthAdjust="spacingAndGlyphs">03</text>
    <text class="norm-text">
      <tspan x="849" y="720">IAM <tspan class="hl-navy">CURIOUS</tspan></tspan>
      <tspan x="849" y="736">ABOUT OTHER'S</tspan>
      <tspan x="849" y="753">PERSPECTIVES</tspan>
      <tspan x="849" y="770">AND NEW WAYS</tspan>
      <tspan x="849" y="786">OF DOING THINGS</tspan>
    </text>
  </g>

  <!-- company name -->
  <text class="label company-name" x="200" y="820" font-size="27" fill="var(--red)">Halvern Quist</text>
</svg>
</body>
</html>
```